Fallow Business Card Design

Photography business needs a logo. I would like to see creative licence on options on 1 & 2 sided. I really like the concept of a fully / partially frosted design. I have already used Brandloom for my Logo, so I am looking for the same level of assistance with this project.

Industry/Entity Type

Business

Font styles to use
Serif
Script

Requirements
Must have
• Must Have:
• - These are my contact details
• Name: Pat L Fallow
• Mobile: 5183920471
• email: marlaquist@postvane.com

```html
<!DOCTYPE html>
<html lang="en">
<head>
<meta charset="utf-8">
<title>Fallow Business Card</title>
<link rel="stylesheet" href="https://fonts.googleapis.com/css2?family=Lato:wght@400;700;900&display=swap">
<style>
  :root {
    --page: #e9e9e7;
    --ink-dark: #2b2b2d;
    --band-dark: #3a3a3c;
    --band-darker: #2f2f31;
    --swirl-light-a: #eef2f8;
    --swirl-light-b: #c9d5e8;
    --swirl-grey-a: #a6abb3;
    --swirl-grey-b: #9299a4;
    --back-edge: #5a5b5e;
    --back-text: #5d5e62;
    --light-text: #f2f2f2;
    --rule: #bfbfbf;
  }
  * { box-sizing: border-box; margin: 0; padding: 0; }
  html, body { width: 900px; height: 1200px; overflow: hidden; }
  body {
    background: var(--page);
    font-family: "Lato", sans-serif;
    position: relative;
  }
  .card {
    position: absolute;
    left: 100px;
    width: 700px;
    height: 400px;
    overflow: hidden;
    box-shadow: 0 6px 18px rgba(0,0,0,0.18);
  }
  .card--front { top: 110px; background: var(--band-dark); }
  .card--back { top: 670px; background: var(--swirl-grey-a); }

  .front__header {
    position: absolute; inset: 0 0 auto 0; height: 124px;
    background: linear-gradient(160deg, var(--swirl-light-a), var(--swirl-light-b) 55%, var(--swirl-light-a));
  }
  .front__company {
    position: absolute; top: 32px; left: 0; right: 0;
    padding-left: 70px;
    text-align: center;
    font-weight: 900; font-size: 34px; letter-spacing: 0.2px;
    color: var(--ink-dark);
  }
  .front__body {
    position: absolute; top: 124px; left: 0; right: 0; bottom: 0;
    background: linear-gradient(180deg, var(--band-dark), var(--band-darker));
    border-top: 3px solid #555;
  }
  .logo-box {
    position: absolute; left: 42px; top: 46px; width: 306px; height: 162px;
    background: repeating-linear-gradient(135deg, #2c2c2e 0 2px, #3a3a3c 2px 4px);
    display: flex; align-items: center; justify-content: center;
    color: var(--light-text); font-weight: 900; font-size: 25px;
  }
  .contact { position: absolute; left: 400px; top: 60px; right: 0; }
  .contact__name {
    font-weight: 700; font-size: 23px; color: #e6e6e6;
    padding-bottom: 6px; border-bottom: 1px solid var(--rule);
    letter-spacing: 0.3px;
  }
  .contact__line {
    display: flex; align-items: center; gap: 12px;
    margin-top: 14px; font-size: 15px; color: #dcdcdc;
  }
  .contact__line:first-of-type { margin-top: 24px; }
  .contact__line svg { width: 13px; height: 13px; flex: none; }

  .back__edge { position: absolute; inset: 0 0 auto 0; height: 10px; background: var(--back-edge); }
  .back__pattern {
    position: absolute; top: 10px; left: 0; right: 0; bottom: 0;
    background: linear-gradient(170deg, var(--swirl-grey-a), var(--swirl-grey-b) 50%, var(--swirl-grey-a));
  }
  .back__company {
    position: absolute; top: 180px; left: 0; right: 0; padding-left: 40px;
    text-align: center; font-weight: 900; font-size: 38px; color: var(--back-text);
  }
  .back__logo {
    position: absolute; top: 250px; left: 0; right: 0; padding-left: 10px;
    text-align: center; font-weight: 900; font-size: 21px; color: var(--back-text);
  }
</style>
</head>
<body>
  <section class="card card--front">
    <div class="front__header" role="img" aria-label="Pale blue swirling wave pattern"></div>
    <h1 class="front__company">YOUR COMPANY NAME</h1>
    <div class="front__body">
      <div class="logo-box">YOUR LOGO</div>
      <div class="contact">
        <p class="contact__name">PAT L FALLOW</p>
        <p class="contact__line">
          <svg viewBox="0 0 13 13" aria-hidden="true"><rect x="3" y="0.5" width="7" height="12" rx="1.2" fill="#cfcfcf"/><rect x="4.3" y="2" width="4.4" height="4" fill="#3a3a3c"/></svg>
          5183920471
        </p>
        <p class="contact__line">
          <svg viewBox="0 0 13 13" aria-hidden="true"><rect x="0.5" y="2.5" width="12" height="8" fill="#e6e6e6"/><path d="M0.8 2.8 L6.5 7 L12.2 2.8" fill="none" stroke="#3a3a3c" stroke-width="1"/></svg>
          marlaquist@postvane.com
        </p>
      </div>
    </div>
  </section>

  <section class="card card--back">
    <div class="back__edge"></div>
    <div class="back__pattern" role="img" aria-label="Grey-blue swirling wave pattern"></div>
    <p class="back__company">YOUR COMPANY NAME</p>
    <p class="back__logo">YOUR LOGO</p>
  </section>
</body>
</html>
```